Solmira Coast Island Weddings, Inc.

Solmira Coast Island Weddings Business Card design for Cardovelle. Clean, contemporary, creative, colorful (using colors provided). ONE SIDE SHOULD INCLUDE logo, www.solmiracoastweddings.com, @vowsbythecove. OTHER SIDE SHOULD INCLUDE Marisol Tennant. Owner & Officiant. Isabela, Puerto Rico. 555.407.1892. marisol@solmiracoastweddings.com. Colors are blue #58AA9E
and golden #e2bf80)

Target Market(s)

Destination Wedding Clients in the United States

Contact Information for Business Card

Marisol Tennant
Owner & Officiant
Isabela, Puerto Rico
555.407.1892
marisol@solmiracoastweddings.com

Font styles to use
Sans Serif

Requirements
Must have
• Colorful (colors are blue #58AA9E
• and golden #e2bf80), clean, contemporary. ONE SIDE SHOULD INCLUDE logo, www.solmiracoastweddings.com, @vowsbythecove. Other side should include Marisol Tennant. Owner & Officiant. Isabela, Puerto Rico. 555.407.1892. marisol@solmiracoastweddings.com
Nice to have
• I would like to see a version that includes my bio photo, and one that doesn't include the bio photo

```html
<!DOCTYPE html>
<html lang="en">
<head>
<meta charset="utf-8">
<title>Solmira Coast Island Weddings – Business Card</title>
<link rel="stylesheet" href="https://fonts.googleapis.com/css2?family=Arimo:wght@400&display=swap">
<style>
  :root {
    --teal: #46aa97;
    --gold: #e2bf78;
    --paper: #ffffff;
    --frame: #1a1a1a;
    --photo-warm: #c9986a;
    --photo-light: #e7c9a3;
  }
  * { box-sizing: border-box; margin: 0; padding: 0; }
  html, body { width: 1200px; height: 1200px; overflow: hidden; background: var(--paper); }
  body { font-family: "Arimo", Arial, sans-serif; }
  .canvas {
    position: relative; width: 1200px; height: 1200px;
    border: 2px solid var(--frame); background: var(--paper);
  }
  .card { position: absolute; left: 212px; width: 785px; height: 472px; overflow: hidden; }
  .card--front { top: 114px; }
  .card--back { top: 643px; }
  .card__shapes { position: absolute; inset: 0; }
  .card__text { position: absolute; left: 0; width: 100%; text-align: center; white-space: nowrap; line-height: 1; }

  .brand-name { font-size: 56px; letter-spacing: 1px; }
  .brand-tag { font-size: 16px; letter-spacing: 5px; }
  .front .brand-name, .front .brand-tag, .front .link { color: var(--gold); }
  .link { font-size: 21px; }

  .back-brand { position: absolute; left: 400px; width: 400px; text-align: center; color: var(--teal); line-height: 1; }
  .back-brand .brand-name { font-size: 38px; }
  .back-brand .brand-tag { font-size: 12px; letter-spacing: 4px; margin-top: 14px; }

  .portrait {
    position: absolute; left: 43px; top: 98px; width: 169px; height: 168px;
    background: linear-gradient(160deg, var(--photo-light), var(--photo-warm));
  }
  .person { position: absolute; left: 27px; width: 201px; text-align: center; color: var(--teal); line-height: 1; white-space: nowrap; }
  .person__name { top: 283px; font-size: 19px; }
  .person__role { top: 309px; font-size: 13px; }
  .contact { color: var(--teal); font-size: 21px; }
</style>
</head>
<body>
<div class="canvas">

  <section class="card card--front front">
    <svg class="card__shapes" width="785" height="472" viewBox="0 0 785 472">
      <rect width="785" height="472" fill="var(--gold)"/>
      <rect y="63" width="785" height="283" fill="var(--teal)"/>
      <polygon points="211,345 576,345 658,472 129,472" fill="var(--teal)"/>
    </svg>
    <div class="card__text brand-name" style="top:240px;">solmira coast</div>
    <div class="card__text brand-tag" style="top:320px;">ISLAND WEDDINGS</div>
    <div class="card__text link" style="top:387px;">www.solmiracoastweddings.com</div>
    <div class="card__text link" style="top:427px;">@vowsbythecove</div>
  </section>

  <section class="card card--back">
    <svg class="card__shapes" width="785" height="472" viewBox="0 0 785 472">
      <rect width="785" height="472" fill="var(--teal)"/>
      <rect y="62" width="785" height="283" fill="var(--gold)"/>
      <polygon points="211,344 576,344 658,472 129,472" fill="var(--gold)"/>
    </svg>
    <div class="portrait" role="img" aria-label="Portrait photo of Marisol Tennant"></div>
    <div class="person person__name">Marisol Tennant.</div>
    <div class="person person__role">Owner &amp; Officiant. Isabela</div>
    <div class="back-brand" style="top:222px;">
      <div class="brand-name">solmira coast</div>
      <div class="brand-tag">ISLAND WEDDINGS</div>
    </div>
    <div class="card__text contact" style="top:383px;">Puerto Rico. 555.407.1892.</div>
    <div class="card__text contact" style="top:421px;">marisol@solmiracoastweddings.com</div>
  </section>

</div>
</body>
</html>
```